Design LUMAGuidance.com

Looking to build a business professional coach website arround Brightorchard.com , it will some standard pages, about me, a page or 2 on bright orchard, maybe with a download and email grab, contact me....

```html
<!DOCTYPE html>
<html lang="en">
<head>
<meta charset="utf-8">
<title>LUMA Guidance</title>
<link rel="stylesheet" href="https://fonts.googleapis.com/css2?family=Hind:wght@500;600;700&family=Poppins:wght@400;500;600&family=Roboto:wght@400;500;700&display=swap">
<style>
:root{
  --purple:#51247f;
  --purple-dark:#3f1a66;
  --ink:#222;
  --text:#444;
  --muted:#6b6b6b;
  --line:#8a8a8a;
  --black:#000;
  --white:#fff;
  --card:#fafafa;
  --green:#8aa66a;
}
*{margin:0;padding:0;box-sizing:border-box}
html,body{width:1200px;height:3051px;overflow:hidden;background:var(--white)}
body{position:relative;font-family:'Poppins',sans-serif;color:var(--text)}
.abs{position:absolute}
.heading{font-family:'Hind',sans-serif;font-weight:700;color:var(--purple);letter-spacing:.5px}

/* header */
.site-header{left:0;top:0;width:1200px;height:66px;background:var(--white)}
.brand{left:87px;top:13px;display:flex;align-items:center;gap:10px}
.brand-dot{width:38px;height:38px;border-radius:50%;background:var(--purple)}
.brand-name{font-family:'Poppins',sans-serif;font-weight:600;font-size:24px;color:var(--purple);line-height:1}
.nav{right:115px;top:24px;display:flex;gap:40px;font-family:'Roboto',sans-serif;font-weight:700;font-size:15px;color:var(--ink)}

/* hero */
.hero{left:0;top:66px;width:1200px;height:534px;overflow:hidden}
.hero-photo{position:absolute;inset:0;background:linear-gradient(100deg,#c8b3e6 0%,#9d84c9 35%,#8e9a7e 65%,#b9cba3 100%)}
.hero-panel{position:absolute;inset:0}
.hero-title{left:112px;top:96px;font-family:'Hind',sans-serif;font-weight:700;font-size:58px;line-height:63px;color:var(--white)}
.hero-copy{left:112px;top:256px;width:440px;font-size:16px;line-height:25px;color:var(--white)}
.btn-outline{left:112px;top:373px;width:132px;height:38px;border:1.5px solid var(--white);color:var(--white);font-family:'Roboto',sans-serif;font-weight:700;font-size:15px;display:flex;align-items:center;justify-content:center}

/* about */
.about-photo{left:111px;top:703px;width:423px;height:391px;background:linear-gradient(135deg,#9aa4ad,#5c6670 55%,#b4a48c)}
.about-title{left:600px;top:695px;font-size:42px}
.about-copy{left:600px;top:763px;width:489px;font-size:16.5px;line-height:30px;text-align:justify;color:var(--text)}
.btn-fill{background:var(--purple);color:var(--white);display:flex;align-items:center;justify-content:center}
.about-btn{left:597px;top:1052px;width:154px;height:42px;font-weight:500;font-size:17px}

/* services */
.services-title{left:0;width:1200px;top:1293px;text-align:center;font-size:42px}
.service-card{top:1418px;width:314px;height:423px;background:var(--card);box-shadow:0 1px 4px rgba(0,0,0,.14)}
.service-photo{height:226px}
.service-body{padding:20px 32px 0}
.service-name{font-family:'Roboto',sans-serif;font-weight:500;font-size:16.5px;color:var(--ink);margin-bottom:6px}
.service-text{font-size:13.2px;line-height:17px;color:var(--muted);text-align:justify}
.service-btn{margin-top:14px;width:90px;height:23px;font-family:'Roboto',sans-serif;font-weight:700;font-size:10.5px}

/* contact */
.contact-band{left:0;top:1952px;width:1200px;height:646px;background:var(--purple)}
.contact-title{left:0;width:1200px;top:2058px;text-align:center;font-size:42px;color:var(--white)}
.contact-box{left:206px;top:2149px;width:787px;height:326px;background:var(--white)}
.field{width:313px;height:56px;border:1px solid var(--line);font-size:16px;color:#333;padding-left:21px;display:flex;align-items:center}
.verify{left:609px;top:2280px;width:205px;height:51px;border:1px solid #d6d6d6;background:#f9f9f9;box-shadow:0 0 3px rgba(0,0,0,.08);font-family:'Roboto',sans-serif}
.verify-box{position:absolute;left:10px;top:15px;width:19px;height:19px;border:2px solid #c1c1c1;background:var(--white);border-radius:2px}
.verify-label{position:absolute;left:36px;top:18px;font-size:9px;color:#333}
.verify-note{position:absolute;right:8px;bottom:5px;font-size:6px;color:#777;text-align:right;line-height:8px}
.submit{left:609px;top:2366px;width:154px;height:41px;font-family:'Hind',sans-serif;font-weight:700;font-size:18px}

/* footer */
.footer{left:0;top:2598px;width:1200px;height:453px;background:var(--black)}
.newsletter{left:108px;top:2555px;width:977px;height:129px;background:var(--white)}
.newsletter-title{left:150px;top:2578px;font-family:'Hind',sans-serif;font-weight:700;font-size:36px;line-height:44px;color:#2b2b2b;letter-spacing:.5px}
.newsletter-title span{color:var(--purple)}
.news-input{left:601px;top:2598px;width:257px;height:45px;border:1px solid var(--purple);font-family:'Roboto',sans-serif;font-size:15px;color:#666;padding-left:20px;display:flex;align-items:center}
.news-btn{left:858px;top:2598px;width:183px;height:45px;font-family:'Roboto',sans-serif;font-weight:500;font-size:16px}
.footer-brand{left:0;width:1200px;top:2762px;display:flex;flex-direction:column;align-items:center;gap:8px}
.footer-brand .brand-dot{width:50px;height:50px}
.footer-brand .brand-name{font-size:26px}
.social{left:446px;top:2910px;display:flex;gap:33px}
.social i{display:block;width:24px;height:24px;border-radius:50%;background:var(--white)}
.download{left:1064px;top:2910px}
.footer-rule{left:111px;top:2989px;width:973px;height:1px;background:#9a9a9a}
.copyright{left:115px;top:3004px;font-size:16px;color:var(--white)}
</style>
</head>
<body>

<header class="site-header abs">
  <div class="brand abs"><span class="brand-dot"></span><span class="brand-name">LUMA Guidance</span></div>
  <nav class="nav abs"><span>HOME</span><span>ABOUT US</span><span>OUR SERVICES</span><span>CONTACT</span></nav>
</header>

<section class="hero abs">
  <div class="hero-photo" role="img" aria-label="Silhouettes of business people overlaid on a city skyline"></div>
  <svg class="hero-panel" width="1200" height="534" viewBox="0 0 1200 534"><polygon points="0,0 778,0 561,534 0,534" fill="var(--purple)"/></svg>
  <h1 class="hero-title abs">WELCOME TO<br>LUMA GUIDANCE</h1>
  <p class="hero-copy abs">Lorem ipsum dolor sit amet, consectetur adipiscing elit, sed do eiusmod tempor incididunt ut labore et dolore magna aliqua. Ut enim ad minim veniam, quis nostrud</p>
  <div class="btn-outline abs">GET STARTED</div>
</section>

<div class="about-photo abs" role="img" aria-label="Team of colleagues discussing charts in an office meeting"></div>
<h2 class="about-title heading abs">ABOUT US</h2>
<p class="about-copy abs">Sed ut perspiciatis unde omnis iste natus error sit voluptatem accusantium doloremque laudantium, totam rem aperiam, eaque ipsa quae ab illo inventore veritatis et quasi architecto beatae vitae dicta sunt explicabo. Nemo enim ipsam voluptatem quia voluptas sit aspernatur aut odit aut fugit, sed quia consequuntur magni dolores eos qui ratione voluptatem sequi nesciunt. Neque porro quisquam est, qui dolorem ipsum quia dolor sit amet.</p>
<div class="about-btn btn-fill abs">Read More</div>

<h2 class="services-title heading abs">OUR SERVICES</h2>

<article class="service-card abs" style="left:112px">
  <div class="service-photo" role="img" aria-label="Coach reviewing a tablet with a client at a table" style="background:linear-gradient(135deg,#8d8a7a,#c9b79a 60%,#6f7a66)"></div>
  <div class="service-body">
    <h3 class="service-name">Coaching</h3>
    <p class="service-text">Lorem ipsum dolor sit amet, consectetur adipiscing elit, sed do eiusmod tempor incididunt ut labore et dolore magna aliqua. Ut enim ad minim</p>
    <div class="service-btn btn-fill">Read More</div>
  </div>
</article>
<article class="service-card abs" style="left:444px">
  <div class="service-photo" role="img" aria-label="Group learning session in a bright conference room" style="background:linear-gradient(135deg,#d9d6cf,#8c8a86 50%,#4b4f58)"></div>
  <div class="service-body">
    <h3 class="service-name">Learning</h3>
    <p class="service-text">Lorem ipsum dolor sit amet, consectetur adipiscing elit, sed do eiusmod tempor incididunt ut labore et dolore magna aliqua. Ut enim ad minim</p>
    <div class="service-btn btn-fill">Read More</div>
  </div>
</article>
<article class="service-card abs" style="left:775px">
  <div class="service-photo" role="img" aria-label="Hands typing on a laptop keyboard" style="background:linear-gradient(135deg,#6f7f8c,#c7ccd0 55%,#e9d9c8)"></div>
  <div class="service-body">
    <h3 class="service-name">Software</h3>
    <p class="service-text">Lorem ipsum dolor sit amet, consectetur adipiscing elit, sed do eiusmod tempor incididunt ut labore et dolore magna aliqua. Ut enim ad minim</p>
    <div class="service-btn btn-fill">Read More</div>
  </div>
</article>

<section class="contact-band abs"></section>
<h2 class="contact-title heading abs">CONTACT US</h2>
<div class="contact-box abs"></div>
<div class="field abs" style="left:276px;top:2201px">First Name</div>
<div class="field abs" style="left:609px;top:2201px">Phone Number</div>
<div class="field abs" style="left:276px;top:2280px">Last Name</div>
<div class="field abs" style="left:276px;top:2359px">Email</div>
<div class="verify abs"><span class="verify-box"></span><span class="verify-label">I'm not a robot</span><span class="verify-note">Verify<br>Privacy · Terms</span></div>
<div class="submit btn-fill abs">SUBMIT</div>

<footer class="footer abs"></footer>
<div class="newsletter abs"></div>
<h2 class="newsletter-title abs"><span>SIGNUP FOR</span> NEWSLETTER<br>SUBSCRIPTION</h2>
<div class="news-input abs">Email Address</div>
<div class="news-btn btn-fill abs">Subscribe Here</div>

<div class="footer-brand abs"><span class="brand-dot"></span><span class="brand-name">LUMA Guidance</span></div>
<div class="social abs"><i></i><i></i><i></i><i></i><i></i><i></i></div>
<svg class="download abs" width="24" height="24" viewBox="0 0 24 24"><path d="M10 2h4v9h4l-6 7-6-7h4z" fill="var(--white)"/><rect x="1" y="18" width="22" height="5" fill="var(--white)"/></svg>
<div class="footer-rule abs"></div>
<p class="copyright abs">© 2023&nbsp; lumaguidance</p>

</body>
</html>
```